Im open to ideas.. I was thinking on my business cards aswell as my logo. a place for my name. email. phone number and abn..

ive attched a file with my business logo. which i dont love the colours.. i was think a dark background with charcoal letters so something along those colour schumes but im open to ideas..

Business

BRL Constructions

```html
<!DOCTYPE html>
<html lang="en">
<head>
<meta charset="utf-8">
<title>BRL Constructions — Business Card</title>
<link href="https://fonts.googleapis.com/css2?family=Open+Sans:wght@400;600;700;800&display=swap" rel="stylesheet">
<style>
  :root {
    --backdrop: #e4e4ea;
    --card-dark: #231f20;
    --card-mid: #3a3637;
    --brand-red: #ec1c24;
    --ink-dark: #231f20;
    --ink-light: #ffffff;
    --ink-soft: #e9e9e9;
  }
  * { margin: 0; padding: 0; box-sizing: border-box; }
  html, body {
    width: 1200px; height: 1200px; overflow: hidden;
    background: var(--backdrop);
    font-family: "Open Sans", sans-serif;
  }
  .canvas { position: relative; width: 1200px; height: 1200px; }

  /* Standalone brand name */
  .brand-lockup {
    position: absolute; top: 120px; right: 80px;
    display: flex; align-items: center; gap: 16px;
  }
  .brand-lockup .brand-square {
    width: 30px; height: 30px; background: var(--brand-red);
  }
  .brand-lockup .brand-name {
    font-weight: 800; font-size: 42px; color: var(--ink-dark);
    letter-spacing: 1px; line-height: 1;
  }

  /* Shared card */
  .card {
    position: absolute; width: 600px; height: 343px; border-radius: 6px;
    overflow: hidden; color: var(--ink-light);
    background: linear-gradient(120deg, var(--card-mid) 0%, var(--card-dark) 60%);
    box-shadow: 0 14px 30px rgba(0,0,0,0.25);
  }

  /* Card front */
  .card-front { top: 240px; left: 80px; }
  .card-front .front-name {
    position: absolute; inset: 0;
    display: flex; align-items: center; justify-content: center; gap: 14px;
  }
  .card-front .brand-square { width: 24px; height: 24px; background: var(--brand-red); }
  .card-front .brand-name { font-weight: 800; font-size: 36px; letter-spacing: 1px; }

  /* Card back */
  .card-back { top: 680px; left: 520px; }
  .card-back .back-brand {
    position: absolute; top: 96px; left: 40px;
    display: flex; align-items: center; gap: 12px;
  }
  .card-back .brand-square { width: 20px; height: 20px; background: var(--brand-red); }
  .card-back .brand-name { font-weight: 800; font-size: 28px; letter-spacing: 1px; }

  .holder {
    position: absolute; top: 44px; right: 40px; text-align: right;
  }
  .holder .holder-name {
    font-weight: 700; font-size: 28px; letter-spacing: 0.5px; line-height: 1.05;
  }
  .holder .holder-title {
    font-weight: 700; font-size: 15px; color: var(--brand-red);
    text-transform: uppercase; letter-spacing: 0.5px;
  }

  .contact-row {
    position: absolute; top: 172px; left: 30px; right: 30px;
    display: flex; justify-content: space-between; align-items: flex-end;
  }
  .contact-item {
    display: flex; flex-direction: column; align-items: center; gap: 8px;
    font-weight: 600; font-size: 13px; color: var(--ink-soft);
  }
  .contact-item .icon {
    width: 36px; height: 36px; border-radius: 50%; background: var(--brand-red);
    display: flex; align-items: center; justify-content: center;
  }

  .address-band {
    position: absolute; left: 0; right: 0; top: 248px; height: 52px;
    background: var(--brand-red);
    display: flex; align-items: center; justify-content: center;
    font-weight: 700; font-size: 18px; color: var(--ink-light); letter-spacing: 0.3px;
  }
</style>
</head>
<body>
<main class="canvas">

  <div class="brand-lockup">
    <span class="brand-square"></span>
    <span class="brand-name">BRL Constructions</span>
  </div>

  <section class="card card-front" aria-label="Business card front">
    <div class="front-name">
      <span class="brand-square"></span>
      <span class="brand-name">BRL Constructions</span>
    </div>
  </section>

  <section class="card card-back" aria-label="Business card back">
    <div class="holder">
      <div class="holder-name">DANIEL REYES</div>
      <div class="holder-title">Sales Manager</div>
    </div>

    <div class="back-brand">
      <span class="brand-square"></span>
      <span class="brand-name">BRL Constructions</span>
    </div>

    <div class="contact-row">
      <div class="contact-item">
        <span class="icon">
          <svg width="20" height="14" viewBox="0 0 20 14" aria-hidden="true">
            <rect x="0.5" y="0.5" width="19" height="13" fill="none" stroke="#fff" stroke-width="1.6"/>
            <polyline points="1,1 10,8 19,1" fill="none" stroke="#fff" stroke-width="1.6"/>
          </svg>
        </span>
        <span>info@brlconstructions.com</span>
      </div>
      <div class="contact-item">
        <span class="icon">
          <svg width="14" height="20" viewBox="0 0 14 20" aria-hidden="true">
            <rect x="1" y="1" width="12" height="18" rx="2" fill="none" stroke="#fff" stroke-width="1.6"/>
            <circle cx="7" cy="16" r="1.2" fill="#fff"/>
          </svg>
        </span>
        <span>(555) 014-2380</span>
      </div>
      <div class="contact-item">
        <span class="icon">
          <svg width="20" height="20" viewBox="0 0 20 20" aria-hidden="true">
            <circle cx="10" cy="10" r="8.5" fill="none" stroke="#fff" stroke-width="1.5"/>
            <ellipse cx="10" cy="10" rx="4" ry="8.5" fill="none" stroke="#fff" stroke-width="1.3"/>
            <line x1="1.5" y1="10" x2="18.5" y2="10" stroke="#fff" stroke-width="1.3"/>
            <line x1="3" y1="5.5" x2="17" y2="5.5" stroke="#fff" stroke-width="1.1"/>
            <line x1="3" y1="14.5" x2="17" y2="14.5" stroke="#fff" stroke-width="1.1"/>
          </svg>
        </span>
        <span>www.brlconstructions.com</span>
      </div>
    </div>

    <div class="address-band">24 Alder Lane Milford, NH 03055-0412</div>
  </section>

</main>
</body>
</html>
```